Business Card for KV

We need a double sided business card:

First Name Last Name
Cell 123-456-7890
firstname@emailaddress.com

License #1234-ABCD-4567
WFRSL # 12345
Alden County

```html
<!DOCTYPE html>
<html lang="en">
<head>
<meta charset="utf-8">
<title>Kindred Valley – Business Card</title>
<link href="https://fonts.googleapis.com/css2?family=Oswald:wght@300;400;500&display=swap" rel="stylesheet">
<style>
  :root {
    --backdrop: #e3e3e3;
    --navy: #2c4a63;
    --olive: #9a9b3c;
    --paper: #f4f4f4;
    --ink: #2c4a63;
  }
  * { margin: 0; padding: 0; box-sizing: border-box; }
  html, body { width: 1200px; height: 960px; overflow: hidden; }
  body {
    background: var(--backdrop);
    position: relative;
    font-family: "Oswald", sans-serif;
  }
  .card { position: absolute; }
  .card-front {
    left: 149px; top: 431px; width: 543px; height: 310px;
    background: var(--navy);
    display: flex; flex-direction: column; align-items: center; justify-content: center;
    gap: 14px;
  }
  .card-back {
    left: 740px; top: 209px; width: 311px; height: 542px;
    background: var(--paper);
    display: flex; flex-direction: column; align-items: center;
  }
  .brand-dot {
    width: 70px; height: 70px; border-radius: 50%;
    background: var(--olive);
  }
  .brand-name {
    font-weight: 500; letter-spacing: 3px; text-transform: uppercase;
  }
  .card-front .brand-name { color: #ffffff; font-size: 42px; }
  .card-back .brand-block {
    margin-top: 48px;
    display: flex; flex-direction: column; align-items: center; gap: 12px;
  }
  .card-back .brand-dot { width: 56px; height: 56px; }
  .card-back .brand-name { color: var(--navy); font-size: 28px; letter-spacing: 2px; }
  .contact {
    margin-top: 128px; text-align: center;
  }
  .contact-name { color: var(--ink); font-size: 25px; line-height: 34px; font-weight: 500; letter-spacing: 0.5px; }
  .contact-phone { color: var(--olive); font-size: 22px; line-height: 28px; font-weight: 400; }
  .contact-email { color: var(--ink); font-size: 15px; line-height: 20px; font-weight: 300; }
  .credentials {
    margin-top: 30px; width: 201px; list-style: none;
    border-top: 1.5px solid var(--olive);
  }
  .credentials li {
    height: 31px; line-height: 30px; text-align: center;
    color: var(--ink); font-size: 15px; font-weight: 300;
    border-bottom: 1.5px solid var(--olive);
  }
</style>
</head>
<body>
  <section class="card card-front" aria-label="Business card front">
    <div class="brand-dot"></div>
    <div class="brand-name">Kindred Valley</div>
  </section>

  <section class="card card-back" aria-label="Business card back">
    <div class="brand-block">
      <div class="brand-dot"></div>
      <div class="brand-name">Kindred Valley</div>
    </div>
    <div class="contact">
      <div class="contact-name">DANIEL CARTER</div>
      <div class="contact-phone">123-456-7890</div>
      <div class="contact-email">firstname@emailaddress.com</div>
    </div>
    <ul class="credentials">
      <li>License #1234-ABCD-4567</li>
      <li>WFRSL # 12345</li>
      <li>Alden County</li>
    </ul>
  </section>
</body>
</html>
```